Business card design needed

Hi.
We need a business card for a building and construction business which specialises in all aspects of domestic building. This includes new and existing works, insurance and shop front works.
We would like to see designs similar to the pic attached.the idea that we are having is a universal card that can be used on shirts,the side of a ute and trailer,fridge magnets this like this, this card will need to be easy to read from advertising point of veiw ie ( ute in transit) a mixer of Blue's would be the main colours for any logo's or graphics and light colours or even white as the back ground choice as we want to stand out against white car. and easy to read while traveling please find some samples of what we like

Target Market(s)

other builders, home owners, insurance builders, anyone who may need work done to their properties home or business

Industry/Entity Type

Construction

Contact Information for Business Card

Company name: Leonard Varga Constructions
Name: Leonard Varga
Mobile: 0461730295
Address: POBox 847 Werribee
Email: leonardvarga@mailnest.com.au

Requirements
Must have
• Must have:
Name: Leonard Varga
Mobile: 0461730295
ABN: 57 308 916 421
The background needs to be able to be put onto car doors and onto tshirts.
Nice to have
• could have a slogan like "the person to bring ur dreams to reality" "done right the first time" "for allMatainace and construction needs" doesnt have to be one of those but something like that
Should not have
• nothing like clip art or basic font

```html
<!DOCTYPE html>
<html lang="en">
<head>
<meta charset="utf-8">
<title>Leonard Varga Constructions – Business Card</title>
<link rel="stylesheet" href="https://fonts.googleapis.com/css2?family=Saira:wght@400;500;600;700&display=swap">
<style>
  :root {
    --navy: #1f2b8c;
    --royal: #2a47b8;
    --sky: #3aa0e0;
    --ice: #7fc8f2;
    --ink: #3b3b45;
    --grey: #55565e;
    --paper: #ffffff;
    --backdrop: #ece9e4;
  }
  * { box-sizing: border-box; margin: 0; padding: 0; }
  html, body {
    width: 1200px; height: 836px; overflow: hidden;
    background: var(--backdrop);
  }
  body { position: relative; font-family: "Saira", "Arial Narrow", sans-serif; }

  .card {
    position: absolute; left: 100px; top: 112px;
    width: 1000px; height: 611px;
    background: var(--paper);
    overflow: hidden;
    box-shadow: 0 10px 30px rgba(0,0,0,.18);
  }
  .card__swoosh { position: absolute; inset: 0; width: 100%; height: 100%; }

  .brand { position: absolute; left: 44px; top: 22px; }
  .brand__name {
    font-size: 62px; font-weight: 600; color: var(--navy);
    line-height: 1; letter-spacing: -0.5px; white-space: nowrap;
  }
  .brand__services {
    margin-top: 8px; font-size: 25px; font-weight: 400; color: var(--ink);
    white-space: nowrap;
  }
  .brand__services .dot { margin: 0 6px; }

  .contact-person {
    position: absolute; left: 262px; top: 160px; width: 500px;
  }
  .contact-person__name {
    text-align: center; font-size: 50px; font-weight: 500; color: var(--navy);
    line-height: 1; padding-bottom: 12px;
    border-bottom: 2px solid var(--grey);
  }
  .phone {
    display: flex; align-items: center; gap: 18px; margin-top: 10px;
  }
  .phone__icon { width: 62px; height: 62px; flex: none; }
  .phone__number {
    font-size: 74px; font-weight: 700; color: var(--navy);
    line-height: 1; letter-spacing: 1px; white-space: nowrap;
  }

  .details {
    position: absolute; left: 44px; top: 372px;
    display: grid; grid-template-columns: auto auto; column-gap: 12px; row-gap: 4px;
    font-size: 28px; line-height: 1.25;
  }
  .details__label { font-weight: 600; color: var(--navy); }
  .details__value { font-weight: 400; color: var(--grey); }

  .emblem {
    position: absolute; left: 680px; top: 360px;
    width: 220px; height: 220px; border-radius: 50%;
    background: radial-gradient(circle at 40% 35%, #6fb3ee 0%, #2f6fd1 55%, #1c3a9e 100%);
    box-shadow: 0 0 0 8px rgba(255,255,255,.25);
  }
</style>
</head>
<body>
  <main class="card">
    <svg class="card__swoosh" viewBox="0 0 1000 611" aria-hidden="true">
      <defs>
        <linearGradient id="swooshFill" x1="1" y1="0" x2="0" y2="1">
          <stop offset="0" stop-color="#1e2a8a"/>
          <stop offset=".55" stop-color="#2a55c2"/>
          <stop offset="1" stop-color="#4a8fe0"/>
        </linearGradient>
      </defs>
      <path d="M1000 150 C900 230 880 400 720 500 C610 568 470 592 300 611 L1000 611 Z" fill="url(#swooshFill)"/>
      <path d="M940 150 C870 250 830 400 690 480 C580 545 440 568 260 590" fill="none" stroke="var(--navy)" stroke-width="5"/>
      <path d="M965 150 C890 255 855 410 705 492 C595 555 460 580 280 600" fill="none" stroke="var(--sky)" stroke-width="8"/>
      <path d="M985 150 C905 260 872 420 715 500" fill="none" stroke="var(--ice)" stroke-width="4"/>
    </svg>

    <header class="brand">
      <h1 class="brand__name">Leonard Varga Constructions</h1>
      <p class="brand__services">Construction<span class="dot">•</span>Renovations<span class="dot">•</span>Insurance Work<span class="dot">•</span>All Forms of Carpentry</p>
    </header>

    <section class="contact-person">
      <h2 class="contact-person__name">Leonard Varga</h2>
      <div class="phone">
        <svg class="phone__icon" viewBox="0 0 62 62" aria-hidden="true">
          <circle cx="31" cy="31" r="31" fill="var(--navy)"/>
          <rect x="21" y="12" width="20" height="38" rx="4" fill="#fff"/>
          <rect x="24" y="16" width="14" height="12" rx="1" fill="var(--navy)"/>
          <g fill="var(--navy)">
            <rect x="24" y="31" width="3" height="3"/><rect x="29.5" y="31" width="3" height="3"/><rect x="35" y="31" width="3" height="3"/>
            <rect x="24" y="36" width="3" height="3"/><rect x="29.5" y="36" width="3" height="3"/><rect x="35" y="36" width="3" height="3"/>
            <rect x="24" y="41" width="3" height="3"/><rect x="29.5" y="41" width="3" height="3"/><rect x="35" y="41" width="3" height="3"/>
          </g>
        </svg>
        <span class="phone__number">046 173 0295</span>
      </div>
    </section>

    <dl class="details">
      <dt class="details__label">Address</dt><dd class="details__value">: PO Box 847 Kelmont Vale</dd>
      <dt class="details__label">Email</dt><dd class="details__value">: leonardvarga@mailnest.com.au</dd>
      <dt class="details__label">ABN</dt><dd class="details__value">: 57 308 916 421</dd>
    </dl>

    <div class="emblem" role="img" aria-label="Round blue emblem with a white tower crane icon"></div>
  </main>
</body>
</html>
```